Martial art rank diploma

Need a diploma for a martial arts belt rank . The art is Japanese in origin , traditional is good , stylish , eye catching .
Dragons are good , no cartoon figures . Tacky is not good . Something proud to display
No martial art poses
Must have place for date , head instructor signature

And must say (a blank for students name )
"Having confirmed with all standards and requirements set forth by Brevant Martial Arts and Fitness , is hereby promoted to the rank of " ( a blank for the rank)
Updates

Project Deadline Extended
Reason: nice designs, need to see more to compare

Industry/Entity Type

Martial Art

Requirements
Must have
• Logo attached and name of the school
Nice to have
• Dragon , that does not look like a centipede .

maybe best to have a dragon in the background as a water mark type of thing.
Should not have
• Tacky look or cartoon figures, or any martial art poses

```html
<!DOCTYPE html>
<html lang="en">
<head>
<meta charset="utf-8">
<title>Belt Rank Diploma – Brevant Martial Arts and Fitness</title>
<link rel="stylesheet" href="https://fonts.googleapis.com/css2?family=Russo+One&family=Ubuntu:ital,wght@0,700;1,500;1,700&display=swap">
<style>
  :root {
    --page-bg: #efefef;
    --paper: #fbb98a;
    --watermark: #f3a778;
    --band-light: #ffffff;
    --band-shade: #e4e3e1;
    --band-edge: #a8a8a8;
    --ink: #5d5d60;
    --accent: #e2552b;
    --title-outline: #f4f2f0;
  }
  * { margin: 0; padding: 0; box-sizing: border-box; }
  html, body {
    width: 1200px; height: 1000px; overflow: hidden;
    background: var(--page-bg);
  }
  .diploma {
    position: absolute; left: 82px; top: 95px;
    width: 1051px; height: 813px;
    background: var(--paper);
    overflow: hidden;
  }
  .diploma__watermark {
    position: absolute; left: 230px; top: 20px;
    width: 820px; height: 790px;
  }
  .diploma__band {
    position: absolute; left: 0; top: 0;
    width: 320px; height: 813px;
  }
  .school-name {
    position: absolute; left: 118px; top: 395px;
    transform: translate(-50%, -50%) rotate(-90deg);
    white-space: nowrap;
    font-family: "Ubuntu", sans-serif; font-weight: 700;
    font-size: 40px; color: var(--ink);
  }
  .school-mark {
    position: absolute; left: 78px; top: 680px;
    width: 80px; height: 80px; border-radius: 50%;
    border: 7px solid var(--ink);
  }
  .diploma__title {
    position: absolute; left: 255px; top: 100px; width: 790px;
    text-align: center;
    font-family: "Russo One", sans-serif;
    font-size: 76px; letter-spacing: 1px;
    color: var(--ink);
    transform: skewX(-12deg);
    -webkit-text-stroke: 0;
    text-shadow:
      3px 0 0 var(--title-outline), -3px 0 0 var(--title-outline),
      0 3px 0 var(--title-outline), 0 -3px 0 var(--title-outline),
      2px 2px 0 var(--title-outline), -2px -2px 0 var(--title-outline),
      2px -2px 0 var(--title-outline), -2px 2px 0 var(--title-outline);
  }
  .field { position: absolute; text-align: center; }
  .field__line { height: 2px; background: var(--ink); }
  .field__label {
    margin-top: 6px;
    font-family: "Ubuntu", sans-serif; font-style: italic; font-weight: 700;
    font-size: 15px; color: var(--accent);
  }
  .field--student { left: 355px; top: 335px; width: 580px; }
  .field--rank { left: 458px; top: 574px; width: 338px; }
  .field--date { left: 233px; top: 742px; width: 339px; }
  .field--instructor { left: 681px; top: 740px; width: 339px; }
  .diploma__statement {
    position: absolute; left: 255px; top: 412px; width: 756px;
    text-align: center;
    font-family: "Ubuntu", sans-serif; font-style: italic; font-weight: 500;
    font-size: 22px; line-height: 23px; letter-spacing: 0.6px;
    color: var(--ink);
  }
</style>
</head>
<body>
  <main class="diploma">
    <svg class="diploma__watermark" role="img" aria-label="Faint dragon watermark in the background" viewBox="0 0 820 790">
      <defs>
        <radialGradient id="watermark-fill" cx="50%" cy="50%" r="50%">
          <stop offset="0%" stop-color="var(--watermark)" stop-opacity="0.9"/>
          <stop offset="100%" stop-color="var(--watermark)" stop-opacity="0"/>
        </radialGradient>
      </defs>
      <rect width="820" height="790" fill="url(#watermark-fill)"/>
    </svg>

    <svg class="diploma__band" viewBox="0 0 320 813" aria-hidden="true">
      <defs>
        <linearGradient id="band-fill" x1="0" y1="0" x2="0" y2="1">
          <stop offset="0%" stop-color="var(--band-shade)"/>
          <stop offset="100%" stop-color="var(--band-light)"/>
        </linearGradient>
      </defs>
      <path d="M0 0 H208 Q300 400 188 813 H0 Z" fill="var(--band-edge)"/>
      <path d="M0 0 H180 Q272 400 160 813 H0 Z" fill="url(#band-fill)"/>
    </svg>

    <div class="school-name">Brevant Martial Arts &amp; Fitness</div>
    <div class="school-mark" aria-hidden="true"></div>

    <h1 class="diploma__title">BELT RANK DIPLOMA</h1>

    <div class="field field--student">
      <div class="field__line"></div>
      <div class="field__label">Student Name</div>
    </div>

    <p class="diploma__statement">Having confirmed with all standards and requirements set forth by Brevant Martial Arts and Fitness , is hereby promoted to the rank of</p>

    <div class="field field--rank">
      <div class="field__line"></div>
      <div class="field__label">Rank</div>
    </div>

    <div class="field field--date">
      <div class="field__line"></div>
      <div class="field__label">Date</div>
    </div>

    <div class="field field--instructor">
      <div class="field__line"></div>
      <div class="field__label">Head Instructor</div>
    </div>
  </main>
</body>
</html>
```